Verimont Designs business card

Front of card should be logo and back of card should be communication info.
Please note: reverse the logo color. Card should be black and everything else white.

Industry/Entity Type

Custom home design/construction

Contact Information for Business Card

Verimont Designs, LLC 614-382-9017 verimontdesigns@quillmail.example

Requirements
Must have
• Square card, Logo on front, communication info on back and perhaps a mini version of the logo on back also. Black card/white lettering. Double sides square card.
Nice to have
• I want to keep it simple. Our product (custom homes) speak for themselves.

```html
<!DOCTYPE html>
<html lang="en">
<head>
<meta charset="utf-8">
<title>Verimont Designs business card</title>
<link href="https://fonts.googleapis.com/css2?family=Montserrat:wght@400;600;700&display=swap" rel="stylesheet">
<style>
  :root {
    --backdrop: #676567;
    --card: #222222;
    --ink: #ffffff;
  }
  * { margin: 0; padding: 0; box-sizing: border-box; }
  html, body { width: 1200px; height: 900px; overflow: hidden; }
  body {
    background: var(--backdrop);
    position: relative;
    font-family: "Montserrat", sans-serif;
    color: var(--ink);
  }
  .card {
    position: absolute;
    width: 400px;
    height: 400px;
    background: var(--card);
    border-radius: 22px;
  }
  .card--contact { left: 134px; top: 254px; }
  .card--brand { left: 618px; top: 252px; }

  .line { position: absolute; left: 0; width: 100%; text-align: center; white-space: nowrap; }

  .wordmark { font-weight: 600; font-size: 26px; letter-spacing: 0.3px; line-height: 1; }
  .tagline { font-weight: 600; font-size: 19.5px; letter-spacing: 0.6px; line-height: 1; }

  .card--contact .wordmark { top: 60px; }
  .card--contact .tagline { top: 88px; }
  .card--brand .wordmark { top: 241px; }
  .card--brand .tagline { top: 270px; }

  .person-name { top: 134px; font-weight: 700; font-size: 19px; letter-spacing: 0.5px; }
  .person-role { top: 163px; font-weight: 400; font-size: 13.5px; letter-spacing: 0.8px; }

  .divider { position: absolute; left: 0; width: 100%; display: flex; justify-content: center; }
  .divider--contact { top: 200px; }
  .divider--address { top: 300px; }

  .contact-item { font-size: 14px; font-weight: 400; line-height: 1; }
  .contact-phone { top: 232px; }
  .contact-email { top: 251px; }
  .contact-web { top: 270px; }
  .address-line { font-size: 14px; font-weight: 400; line-height: 1; }
  .address-street { top: 332px; }
  .address-city { top: 350px; }
</style>
</head>
<body>
  <section class="card card--contact" aria-label="Card contact side">
    <div class="line wordmark">VERIMONT DESIGNS</div>
    <div class="line tagline">CUSTOM HOME BUILDERS</div>

    <div class="line person-name">Dana Whitfield</div>
    <div class="line person-role">CEO &amp; Founder</div>

    <div class="divider divider--contact">
      <svg width="200" height="20" viewBox="0 0 200 20" aria-hidden="true">
        <rect x="4" y="9" width="42" height="2" fill="#fff"/>
        <rect x="154" y="9" width="42" height="2" fill="#fff"/>
        <circle cx="80" cy="10" r="8.5" fill="#fff"/>
        <path d="M76 7.5 q4 -3 8 0 l-1 2 h-6 z M75.5 11 h9 v3 h-9 z" fill="#222"/>
        <circle cx="100" cy="10" r="8.5" fill="#fff"/>
        <rect x="95" y="6.5" width="10" height="7" rx="1" fill="#222"/>
        <path d="M95.5 7 l4.5 3.5 l4.5 -3.5" stroke="#fff" stroke-width="1" fill="none"/>
        <circle cx="120" cy="10" r="8.5" fill="#fff"/>
        <circle cx="120" cy="10" r="5" fill="none" stroke="#222" stroke-width="1.3"/>
        <path d="M115 10 h10 M120 5 q-3 5 0 10 q3 -5 0 -10" stroke="#222" stroke-width="1" fill="none"/>
      </svg>
    </div>

    <div class="line contact-item contact-phone">614 382 9017</div>
    <div class="line contact-item contact-email">info@verimontmail.example</div>
    <div class="line contact-item contact-web">www.verimontdesigns.example</div>

    <div class="divider divider--address">
      <svg width="160" height="20" viewBox="0 0 160 20" aria-hidden="true">
        <rect x="6" y="9" width="42" height="2" fill="#fff"/>
        <rect x="100" y="9" width="42" height="2" fill="#fff"/>
        <path d="M74 2 a7 7 0 0 1 7 7 c0 5 -7 10 -7 10 s-7 -5 -7 -10 a7 7 0 0 1 7 -7 z" fill="#fff"/>
        <circle cx="74" cy="9" r="2.6" fill="#222"/>
      </svg>
    </div>

    <div class="line address-line address-street">Unit 7, Harrowgate Trade Park</div>
    <div class="line address-line address-city">43215 Columbus Ridge</div>
  </section>

  <section class="card card--brand" aria-label="Card brand side">
    <div class="line wordmark">VERIMONT DESIGNS</div>
    <div class="line tagline">CUSTOM HOME BUILDERS</div>
  </section>
</body>
</html>
```